Profesional personal website needs design and business card

I need a business card with my professional name as a logo "Marlo Vitality" for my business. I am a Wellness Coach, consultant and trainer. So it should be professional, wellness oriented and modern.

Target Market(s)

Private clients, governments, corporations. Luxury and high market.

Industry/Entity Type

Health And Wellness

Contact Information for Business Card

Marlo Vitality should be the logo

Colors

Designer to choose colors to be used in the design.

Requirements
Must have
• Marlo Vitality
• Name: Tomás Arribal
• Wellness Coach, Consultant & Trainer.
• Website: www.marlovitality.example
• Phone:
• Spain (+34) 612 480 397
• (USA) +1 (555) 318 2046
Nice to have
• The most important is the design of "Marlo Vitality", as this is going to be my personal brand logo. It should be professional, wellness, high end and actual.
Should not have
• no golds, no baroque style..

```html
<!DOCTYPE html>
<html lang="en">
<head>
<meta charset="utf-8">
<title>Marlo Vitality – Business Card</title>
<link href="https://fonts.googleapis.com/css2?family=Quicksand:wght@500;600;700&display=swap" rel="stylesheet">
<style>
  :root {
    --page-bg: #e9eaec;
    --card-dark: #1b1b1b;
    --card-light: #ffffff;
    --brand-blue: #2b93cf;
    --accent-blue: #62a9d6;
    --edge-blue: #bfe0f3;
    --shadow: rgba(0, 0, 0, 0.28);
  }
  * { box-sizing: border-box; margin: 0; padding: 0; }
  html, body {
    width: 1200px; height: 913px; overflow: hidden;
    background: var(--page-bg);
    font-family: "Quicksand", sans-serif;
  }
  .canvas { position: relative; width: 1200px; height: 913px; }

  .card {
    position: absolute;
    width: 620px; height: 354px;
    border-radius: 22px;
    overflow: hidden;
    box-shadow: 0 14px 30px var(--shadow);
  }
  .card--back {
    left: 80px; top: 70px;
    background: var(--card-dark);
    display: flex; align-items: center; justify-content: center;
  }
  .card--front {
    left: 500px; top: 480px;
    background: var(--card-light);
    box-shadow: 0 6px 0 var(--edge-blue), 0 18px 32px var(--shadow);
  }

  .wordmark {
    color: var(--brand-blue);
    font-weight: 600;
    letter-spacing: 1px;
    white-space: nowrap;
    line-height: 1;
  }
  .card--back .wordmark { font-size: 64px; }
  .card--front .wordmark {
    position: absolute; left: 40px; top: 42px;
    font-size: 44px;
  }

  .monogram-shape {
    position: absolute;
    right: -90px; top: 40px;
    width: 300px; height: 300px;
    border-radius: 50%;
    border: 34px solid var(--accent-blue);
  }

  .identity {
    position: absolute; left: 66px; top: 150px;
    color: var(--brand-blue);
  }
  .identity__name { font-size: 27px; font-weight: 700; letter-spacing: 0.5px; }
  .identity__role { font-size: 15px; font-weight: 500; margin-top: 4px; letter-spacing: 0.4px; }

  .marker {
    position: absolute; left: 0; top: 150px;
    width: 10px; height: 56px;
    background: var(--brand-blue);
    border-radius: 0 4px 4px 0;
  }

  .contacts {
    position: absolute; left: 66px; bottom: 36px;
    list-style: none;
    color: var(--brand-blue);
    font-size: 17px; font-weight: 500;
    letter-spacing: 0.6px;
  }
  .contacts__item { display: flex; align-items: center; gap: 10px; margin-top: 6px; }
  .contacts__icon { width: 16px; height: 16px; flex: none; fill: var(--brand-blue); }
</style>
</head>
<body>
<main class="canvas">
  <section class="card card--back" aria-label="Card back">
    <span class="wordmark">Marlo Vitality</span>
  </section>

  <section class="card card--front" aria-label="Card front">
    <span class="wordmark">Marlo Vitality</span>
    <div class="monogram-shape" aria-hidden="true"></div>
    <div class="marker" aria-hidden="true"></div>

    <div class="identity">
      <p class="identity__name">Tomás Arribal</p>
      <p class="identity__role">Wellness Coach, Consultant &amp; Trainer</p>
    </div>

    <ul class="contacts">
      <li class="contacts__item">
        <svg class="contacts__icon" viewBox="0 0 24 24" aria-hidden="true"><path d="M6.6 10.8a15.1 15.1 0 0 0 6.6 6.6l2.2-2.2a1 1 0 0 1 1-.25 11.4 11.4 0 0 0 3.6.57 1 1 0 0 1 1 1V20a1 1 0 0 1-1 1A17 17 0 0 1 3 4a1 1 0 0 1 1-1h3.5a1 1 0 0 1 1 1c0 1.25.2 2.45.57 3.6a1 1 0 0 1-.25 1z"/></svg>
        <span>(+34) 612 480 397 (Spain)</span>
      </li>
      <li class="contacts__item">
        <svg class="contacts__icon" viewBox="0 0 24 24" aria-hidden="true"><path d="M6.6 10.8a15.1 15.1 0 0 0 6.6 6.6l2.2-2.2a1 1 0 0 1 1-.25 11.4 11.4 0 0 0 3.6.57 1 1 0 0 1 1 1V20a1 1 0 0 1-1 1A17 17 0 0 1 3 4a1 1 0 0 1 1-1h3.5a1 1 0 0 1 1 1c0 1.25.2 2.45.57 3.6a1 1 0 0 1-.25 1z"/></svg>
        <span>+1 (555) 318 2046 (USA)</span>
      </li>
      <li class="contacts__item">
        <svg class="contacts__icon" viewBox="0 0 24 24" aria-hidden="true"><circle cx="12" cy="12" r="10" fill="none" stroke="#2b93cf" stroke-width="2"/><path d="M2 12h20M12 2c3 3 3 17 0 20M12 2c-3 3-3 17 0 20" fill="none" stroke="#2b93cf" stroke-width="1.6"/></svg>
        <span>www.marlovitality.example</span>
      </li>
    </ul>
  </section>
</main>
</body>
</html>
```